"Fight Back" banner ad design

We have sketched the design and have images to consider including. We are looking for something striking, FIGHT BACK! with a clenched fist image, then a fading images of variance.png and hi-bill.png in the background. Tag line "Fight your water bill with your own data" optionally include "Crest View" rivo3159 logo, KMPT Design, LLC based in San Diego CA. Pre-order now, visit https://www.raisenest.com/rivoplume @rivo3159, info@rivo3159.com

"Fight your water bill with your own data"

```html
<!DOCTYPE html>
<html lang="en">
<head>
<meta charset="utf-8">
<title>Fight Your Water Bill – Banner Set</title>
<link href="https://fonts.googleapis.com/css2?family=Oswald:wght@600&family=Open+Sans:wght@400;600&family=Arimo:wght@400;700&display=swap" rel="stylesheet">
<style>
:root{
  --page:#e3e3e3;
  --paper:#f6f6f6;
  --teal:#2f92a7;
  --teal-light:#4bb3c7;
  --teal-pale:#8fd0de;
  --deep:#063a48;
  --frame:#1e5564;
  --ink:#2f2f2f;
  --grid:#9aa3a6;
}
*{margin:0;padding:0;box-sizing:border-box}
html,body{width:1200px;height:1046px;overflow:hidden;background:var(--page)}
body{position:relative;font-family:"Open Sans",sans-serif;color:var(--ink)}
.banner{position:absolute;left:38px;width:1125px;height:470px;overflow:hidden;box-shadow:0 2px 6px rgba(0,0,0,.25);background:var(--paper)}
.banner--lines{top:32px}
.banner--bars{top:539px}
.stage{position:absolute;left:0;top:0;width:1406px;height:587px;transform:scale(.8);transform-origin:0 0}
.stage>svg{position:absolute;left:0;top:0}
.brand{position:absolute;left:72px;top:80px;display:flex;align-items:center;gap:18px}
.brand__dot{width:44px;height:44px;border-radius:50%;background:var(--teal)}
.brand__name{font-family:"Open Sans",sans-serif;font-weight:600;font-size:34px;color:var(--teal)}
.headline{position:absolute;left:535px;width:800px;top:14px;text-align:center;font-family:"Oswald",sans-serif;font-weight:600;font-size:42px;line-height:50px;letter-spacing:-1px;white-space:nowrap;color:var(--teal);transform:scaleX(.82);transform-origin:50% 50%}
.subline{position:absolute;left:790px;width:296px;top:62px;line-height:30px;display:flex;align-items:center;gap:14px;font-size:24px;color:#2a2a2a;white-space:nowrap}
.subline::before,.subline::after{content:"";flex:1;height:1px;background:#3c5a64}
.pill{position:absolute;height:30px;border-radius:15px;background:linear-gradient(90deg,var(--teal),var(--teal-light));color:#fff;font-weight:600;font-size:16px;display:flex;align-items:center;justify-content:center;white-space:nowrap}
.pill--fees{left:510px;top:120px;width:339px}
.pill--use{left:934px;top:120px;width:434px}
.pill--due{left:510px;top:532px;width:339px;justify-content:space-between;padding:0 22px 0 16px;font-size:15px}
.fees{position:absolute;left:526px;top:0;width:300px;font-size:11px}
.fees .row{position:absolute;left:0;right:0;height:14px;white-space:nowrap}
.fees .row span{position:absolute;top:0}
.fees .amt{left:264px}
.fees .qty{left:77px}
.fees .unit{left:124px}
.fees .at{left:157px}
.fees .rate{left:180px}
.fees .head{font-weight:600}
.fees .rule{position:absolute;left:0;right:-8px;height:1px;background:#555}
.legend{position:absolute;top:170px;display:flex;gap:32px;font-size:11px;font-weight:600;white-space:nowrap}
.legend span{display:flex;align-items:center;gap:10px}
.legend i{display:block;width:17px;height:17px}
.legend--lines{left:1049px}
.sw-prev{background:var(--teal-light)}
.contact{position:absolute;left:1106px;color:#fff;font-size:16px;display:flex;align-items:center;gap:8px;white-space:nowrap}
.contact--web{top:514px}
.contact--mail{top:545px}
.sheet{position:absolute;left:524px;top:0;width:283px;font-family:"Arimo",sans-serif;font-size:11px;color:#111}
.sheet .row{position:absolute;left:0;right:0;height:13px;white-space:nowrap;line-height:13px}
.sheet .row span{position:absolute;top:0}
.sheet .amt{right:0}
.sheet .in1{left:10px}
.sheet .in2{left:19px}
.sheet .qty{right:161px}
.sheet .unit{left:129px}
.sheet .at{left:158px}
.sheet .rate{left:175px}
.sheet .head{font-weight:700}
.sheet-title{position:absolute;left:523px;top:108px;width:300px;height:15px;background:var(--frame);color:#fff;font-family:"Arimo",sans-serif;font-weight:700;font-size:13px;line-height:15px;text-align:center}
.sheet-due{position:absolute;left:523px;top:529px;width:300px;height:15px;background:var(--teal-pale);border-top:1px solid var(--frame);font-family:"Arimo",sans-serif;font-weight:700;font-size:13px;line-height:14px;display:flex;justify-content:space-between;padding:0 10px 0 2px}
.chart-title{position:absolute;left:863px;top:155px;width:505px;height:22px;background:var(--frame);color:#fff;font-family:"Arimo",sans-serif;font-weight:700;font-size:20px;line-height:22px;text-align:center;white-space:nowrap}
.legend--bars{left:993px;top:181px;font-family:"Arimo",sans-serif;font-size:14px;font-weight:700;gap:16px}
.legend--bars i{width:15px;height:15px;border:1px solid #333}
</style>
</head>
<body>

<section class="banner banner--lines">
  <div class="stage">
    <svg width="1406" height="587" viewBox="0 0 1406 587">
      <defs>
        <linearGradient id="photoTone" x1="0" y1="0" x2="0" y2="1">
          <stop offset="0" stop-color="#f7f7f2"/>
          <stop offset=".3" stop-color="#e6e3b8"/>
          <stop offset=".6" stop-color="#a9b861"/>
          <stop offset="1" stop-color="#b58a4c"/>
        </linearGradient>
      </defs>
      <polygon points="0,0 285,0 450,300 280,587 0,587" fill="url(#photoTone)" role="img" aria-label="Photo of green seedlings growing from stacks of gold coins"/>
      <polygon points="285,0 335,0 497,300 450,300" fill="var(--teal)"/>
      <polygon points="450,300 497,300 330,587 280,587" fill="var(--deep)"/>
      <g stroke="var(--grid)" stroke-width="1">
        <line x1="943" x2="1378" y1="218" y2="218"/><line x1="943" x2="1378" y1="233.7" y2="233.7"/><line x1="943" x2="1378" y1="249.4" y2="249.4"/><line x1="943" x2="1378" y1="265.1" y2="265.1"/><line x1="943" x2="1378" y1="280.8" y2="280.8"/><line x1="943" x2="1378" y1="296.4" y2="296.4"/><line x1="943" x2="1378" y1="312.1" y2="312.1"/><line x1="943" x2="1378" y1="327.8" y2="327.8"/><line x1="943" x2="1378" y1="343.5" y2="343.5"/><line x1="943" x2="1378" y1="359.2" y2="359.2"/><line x1="943" x2="1378" y1="374.9" y2="374.9"/><line x1="943" x2="1378" y1="390.6" y2="390.6"/><line x1="943" x2="1378" y1="406.3" y2="406.3"/><line x1="943" x2="1378" y1="421.9" y2="421.9"/><line x1="943" x2="1378" y1="437.6" y2="437.6"/><line x1="943" x2="1378" y1="453.3" y2="453.3"/>
      </g>
      <g font-family="Open Sans, sans-serif" font-size="9" fill="#333" text-anchor="end">
        <text x="932" y="221">80</text><text x="932" y="237">75</text><text x="932" y="252">70</text><text x="932" y="268">65</text><text x="932" y="284">60</text><text x="932" y="299">55</text><text x="932" y="315">50</text><text x="932" y="331">45</text><text x="932" y="346">40</text><text x="932" y="362">35</text><text x="932" y="378">30</text><text x="932" y="394">25</text><text x="932" y="409">20</text><text x="932" y="425">15</text><text x="932" y="441">10</text><text x="932" y="456">5</text><text x="932" y="472">0</text>
      </g>
      <polyline points="956,384.3 1032,362.3 1112,412.5 1191,374.9 1269,390.6 1347,390.6" fill="none" stroke="var(--teal-light)" stroke-width="1.5"/>
      <g fill="var(--teal-light)"><circle cx="956" cy="384.3" r="3"/><circle cx="1032" cy="362.3" r="3"/><circle cx="1112" cy="412.5" r="3"/><circle cx="1191" cy="374.9" r="3"/><circle cx="1269" cy="390.6" r="3"/><circle cx="1347" cy="390.6" r="3"/></g>
      <polyline points="975,396.8 1054,406.3 1133,406.3 1209,218 1288,252.5 1367,236.8" fill="none" stroke="#126c80" stroke-width="1.5"/>
      <g fill="#126c80"><circle cx="975" cy="396.8" r="3"/><circle cx="1054" cy="406.3" r="3"/><circle cx="1133" cy="406.3" r="3"/><circle cx="1209" cy="218" r="3"/><circle cx="1288" cy="252.5" r="3"/><circle cx="1367" cy="236.8" r="3"/></g>
      <polyline points="993,587 1053,503 1093,503" fill="none" stroke="var(--teal)" stroke-width="1.5"/>
      <polygon points="1093,500 1406,497 1406,587 1040,587" fill="var(--deep)"/>
      <line x1="1093" y1="500" x2="1406" y2="497" stroke="var(--teal)" stroke-width="4"/>
    </svg>

    <div class="brand"><span class="brand__dot"></span><span class="brand__name">Rivo3159</span></div>
    <h1 class="headline">FIGHT YOUR WATER BILL WITH YOUR OWN DATA</h1>
    <p class="subline">CREST VIEW</p>

    <div class="pill pill--fees">FEES &amp; CHARGES</div>
    <div class="fees">
      <div class="row head" style="top:167px"><span>Water Services</span></div>
      <div class="row" style="top:188px"><span>Single Family Residential Base Fee</span><span class="amt">48.44</span></div>
      <div class="row" style="top:219px"><span>Water Used</span><span class="qty">65</span><span class="unit">HCF</span></div>
      <div class="row" style="top:238px"><span>Tier 1</span><span class="qty">8.00</span><span class="unit">HCF</span><span class="at">@</span><span class="rate">$4.8425</span><span class="amt">38.74</span></div>
      <div class="row" style="top:257px"><span>Tier 2</span><span class="qty">16.00</span><span class="unit">HCF</span><span class="at">@</span><span class="rate">$5.4231</span><span class="amt">86.77</span></div>
      <div class="row" style="top:276px"><span>Tier 3</span><span class="qty">12.00</span><span class="unit">HCF</span><span class="at">@</span><span class="rate">$7.7483</span><span class="amt">92.98</span></div>
      <div class="row" style="top:295px"><span>Tier 4</span><span class="qty">29.00</span><span class="unit">HCF</span><span class="at">@</span><span class="rate">10.8952</span><span class="amt">315.96</span></div>
      <div class="rule" style="top:321px"></div>
      <div class="row" style="top:333px"><span>Total Charge for Water Used</span><span class="amt">534.45</span></div>
      <div class="row head" style="top:374px"><span>Sewer &amp; Storm Drain Services</span></div>
      <div class="row" style="top:395px"><span>Sewer Base Fee</span><span class="amt">30.66</span></div>
      <div class="row" style="top:414px"><span>Sewer Service Charge</span><span class="amt">60.17</span></div>
      <div class="row" style="top:433px"><span>Sewer Drain</span><span class="amt">1.90</span></div>
      <div class="row head" style="top:474px"><span>Total Current Charges</span><span class="amt">675.62</span></div>
      <div class="row" style="top:494px"><span>Deferred Due</span><span class="amt">79.66</span></div>
    </div>
    <div class="pill pill--due"><span>TOTAL DUE</span><span>755.28</span></div>

    <div class="pill pill--use">WATER USE IN HCF ( Hundred Cubic Feet )</div>
    <div class="legend legend--lines"><span><i class="sw-prev"></i>Previous Year</span><span><i style="background:#126c80"></i>Current Year</span></div>

    <p class="contact contact--web">
      <svg width="14" height="14" viewBox="0 0 14 14" fill="none" stroke="#fff" stroke-width="1"><circle cx="7" cy="7" r="6"/><ellipse cx="7" cy="7" rx="2.6" ry="6"/><line x1="1" y1="7" x2="13" y2="7"/></svg>
      www.raisenest.com/rivoplume</p>
    <p class="contact contact--mail">
      <svg width="14" height="14" viewBox="0 0 14 14" fill="none" stroke="#fff" stroke-width="1"><path d="M1 6 L7 1 L13 6 V13 H1 Z"/><path d="M1 6 L7 10 L13 6"/></svg>
      info@rivo3159.com</p>
  </div>
</section>

<section class="banner banner--bars">
  <div class="stage">
    <svg width="1406" height="587" viewBox="0 0 1406 587">
      <defs>
        <linearGradient id="photoTone2" x1="0" y1="0" x2="0" y2="1">
          <stop offset="0" stop-color="#f7f7f2"/>
          <stop offset=".3" stop-color="#e6e3b8"/>
          <stop offset=".6" stop-color="#a9b861"/>
          <stop offset="1" stop-color="#b58a4c"/>
        </linearGradient>
      </defs>
      <polygon points="0,0 285,0 450,300 280,587 0,587" fill="url(#photoTone2)" role="img" aria-label="Photo of green seedlings growing from stacks of gold coins"/>
      <polygon points="285,0 335,0 497,300 450,300" fill="var(--teal)"/>
      <polygon points="450,300 497,300 330,587 280,587" fill="var(--deep)"/>
      <rect x="515.5" y="99.5" width="320" height="454" fill="#fff" stroke="#8a9aa0"/>
      <rect x="521" y="105" width="304" height="440" fill="#fff" stroke="var(--frame)" stroke-width="2"/>
      <line x1="742" y1="230" x2="816" y2="230" stroke="#333"/>
      <rect x="855.5" y="144.5" width="526" height="327" fill="#fff" stroke="#8a9aa0"/>
      <rect x="861" y="152" width="509" height="313" fill="#fff" stroke="var(--frame)" stroke-width="3"/>
      <g stroke="#222" stroke-width="1">
        <line x1="893" x2="1361" y1="203" y2="203"/><line x1="893" x2="1361" y1="219" y2="219"/><line x1="893" x2="1361" y1="235" y2="235"/><line x1="893" x2="1361" y1="251" y2="251"/><line x1="893" x2="1361" y1="267" y2="267"/><line x1="893" x2="1361" y1="283" y2="283"/><line x1="893" x2="1361" y1="299" y2="299"/><line x1="893" x2="1361" y1="315" y2="315"/><line x1="893" x2="1361" y1="331" y2="331"/><line x1="893" x2="1361" y1="347" y2="347"/><line x1="893" x2="1361" y1="363" y2="363"/><line x1="893" x2="1361" y1="379" y2="379"/><line x1="893" x2="1361" y1="395" y2="395"/><line x1="893" x2="1361" y1="411" y2="411"/><line x1="893" x2="1361" y1="427" y2="427"/><line x1="893" x2="1361" y1="443" y2="443"/><line x1="893" x2="1361" y1="459" y2="459"/>
        <line x1="893" x2="893" y1="203" y2="459"/>
      </g>
      <g font-family="Arimo, sans-serif" font-size="13" font-weight="700" fill="#111" text-anchor="end">
        <text x="889" y="208">80</text><text x="889" y="224">75</text><text x="889" y="240">70</text><text x="889" y="256">65</text><text x="889" y="272">60</text><text x="889" y="288">55</text><text x="889" y="304">50</text><text x="889" y="320">45</text><text x="889" y="336">40</text><text x="889" y="352">35</text><text x="889" y="368">30</text><text x="889" y="384">25</text><text x="889" y="400">20</text><text x="889" y="416">15</text><text x="889" y="432">10</text><text x="889" y="448">5</text><text x="889" y="464">0</text>
      </g>
      <g fill="var(--teal-pale)" stroke="#2a4a55">
        <rect x="931" y="372.6" width="16" height="86.4"/><rect x="1010" y="350.2" width="16" height="108.8"/><rect x="1088" y="401.4" width="16" height="57.6"/><rect x="1167" y="363" width="16" height="96"/><rect x="1246" y="379" width="16" height="80"/><rect x="1325" y="379" width="16" height="80"/>
      </g>
      <g fill="var(--frame)" stroke="#0f2f38">
        <rect x="951" y="385.4" width="16" height="73.6"/><rect x="1029" y="395" width="16" height="64"/><rect x="1108" y="395" width="16" height="64"/><rect x="1187" y="203" width="16" height="256"/><rect x="1265" y="238.2" width="16" height="220.8"/><rect x="1344" y="222.2" width="16" height="236.8"/>
      </g>
      <polyline points="993,587 1053,503 1093,503" fill="none" stroke="var(--teal)" stroke-width="1.5"/>
      <polygon points="1093,500 1406,497 1406,587 1040,587" fill="var(--deep)"/>
      <line x1="1093" y1="500" x2="1406" y2="497" stroke="var(--teal)" stroke-width="4"/>
    </svg>

    <div class="brand"><span class="brand__dot"></span><span class="brand__name">Rivo3159</span></div>
    <h2 class="headline">FIGHT YOUR WATER BILL WITH YOUR OWN DATA</h2>
    <p class="subline">CREST VIEW</p>

    <div class="sheet-title">FEES &amp; CHARGES</div>
    <div class="sheet">
      <div class="row head" style="top:126px"><span>Water Services</span></div>
      <div class="row" style="top:139px"><span class="in1">Single Family Residential Base Fee</span><span class="amt">48.44</span></div>
      <div class="row" style="top:152px"><span class="in1">Water Used</span><span class="qty">65</span><span class="unit">HCF</span></div>
      <div class="row" style="top:165px"><span class="in2">Tier 1</span><span class="qty">8.00</span><span class="unit">HCF</span><span class="at">@</span><span class="rate">$4.8425</span><span class="amt">38.74</span></div>
      <div class="row" style="top:178px"><span class="in2">Tier 2</span><span class="qty">16.00</span><span class="unit">HCF</span><span class="at">@</span><span class="rate">$5.4231</span><span class="amt">86.77</span></div>
      <div class="row" style="top:191px"><span class="in2">Tier 3</span><span class="qty">12.00</span><span class="unit">HCF</span><span class="at">@</span><span class="rate">$7.7483</span><span class="amt">92.98</span></div>
      <div class="row" style="top:204px"><span class="in2">Tier 4</span><span class="qty">29.00</span><span class="unit">HCF</span><span class="at">@</span><span class="amt">315.96</span></div>
      <div class="row" style="top:217px"><span style="left:194px">$10.8952</span></div>
      <div class="row" style="top:230px"><span class="in1">Total Charge for Water Used</span><span class="amt" style="right:-8px">534.45</span></div>
      <div class="row head" style="top:260px"><span>Sewer &amp; Storm Drain Services</span></div>
      <div class="row" style="top:273px"><span class="in1">Sewer Base Fee</span><span class="amt">30.66</span></div>
      <div class="row" style="top:286px"><span class="in1">Sewer Service Charge</span><span class="amt">60.17</span></div>
      <div class="row" style="top:298px"><span class="in1">Storm Drain</span><span class="amt">1.90</span></div>
      <div class="row" style="top:336px"><span class="head">Total Current Charges</span><span class="amt">675.62</span></div>
      <div class="row" style="top:349px"><span>Deferred Due</span><span class="amt">79.66</span></div>
    </div>
    <div class="sheet-due"><span>TOTAL DUE</span><span>755.28</span></div>

    <div class="chart-title">WATER USE IN HCF (Hundred Cubic Feet)</div>
    <div class="legend legend--bars"><span><i style="background:var(--teal-pale)"></i>Previous Year</span><span><i style="background:var(--frame)"></i>Current Year</span></div>

    <p class="contact contact--web">
      <svg width="14" height="14" viewBox="0 0 14 14" fill="none" stroke="#fff" stroke-width="1"><circle cx="7" cy="7" r="6"/><ellipse cx="7" cy="7" rx="2.6" ry="6"/><line x1="1" y1="7" x2="13" y2="7"/></svg>
      www.raisenest.com/rivoplume</p>
    <p class="contact contact--mail">
      <svg width="14" height="14" viewBox="0 0 14 14" fill="none" stroke="#fff" stroke-width="1"><path d="M1 6 L7 1 L13 6 V13 H1 Z"/><path d="M1 6 L7 10 L13 6"/></svg>
      info@rivo3159.com</p>
  </div>
</section>

</body>
</html>
```